New cosmetics company needs packaging design

We need a packaging design for our new cosmetics brand. We are looking for modern, sleek packaging such as black or white packaging with gold text. The packaging will be for boxes of different sizes for eye pencils, lipsticks, foundation etc. For example small long rectangle boxes, standing rectangle boxes and square boxes for products.
Attached is a pattern we were thinking to be used on the inside of the boxes and maybe some elements of this pattern on the outside of the boxes. This is not a strict requirement, we are happy to receive other ideas.
Our logo is a 5-letter word and we have a round symbol, which we'll be happy to send after seeing some designs.
Thank you.
Cosmetics

```html
<!DOCTYPE html>
<html lang="en">
<head>
<meta charset="utf-8">
<title>LUVRA – Product Box Label</title>
<link rel="stylesheet" href="https://fonts.googleapis.com/css2?family=Cinzel:wght@500&family=Jost:wght@400;500;700&family=Oswald:wght@600&display=swap">
<style>
  :root {
    --stage: #f1f1f1;
    --stage-edge: #e2e2e2;
    --label-black: #121212;
    --label-black-soft: #1d1d1d;
    --gold: #e2b624;
    --gold-light: #ffe27a;
    --gold-deep: #b8860b;
    --ink-dark: #1a1306;
  }
  * { box-sizing: border-box; margin: 0; padding: 0; }
  html, body {
    width: 857px;
    height: 1200px;
    overflow: hidden;
  }
  body {
    background: radial-gradient(ellipse at center, var(--stage) 40%, var(--stage-edge) 100%);
    position: relative;
    font-family: "Jost", sans-serif;
  }
  .label {
    position: absolute;
    left: 192px;
    top: 45px;
    width: 475px;
    height: 1113px;
    background: linear-gradient(180deg, var(--label-black-soft), var(--label-black) 60%, #0c0c0c);
    box-shadow: 0 2px 8px rgba(0,0,0,0.25);
    overflow: hidden;
  }
  .brand-mark {
    position: absolute;
    left: 169px;
    top: 62px;
    width: 138px;
    height: 138px;
  }
  .brand-name {
    position: absolute;
    left: 0;
    top: 222px;
    width: 100%;
    text-align: center;
    font-family: "Jost", sans-serif;
    font-weight: 400;
    font-size: 78px;
    letter-spacing: 12px;
    padding-left: 12px;
    line-height: 1;
    color: var(--gold);
  }
  .product-name {
    position: absolute;
    left: 0;
    top: 400px;
    width: 100%;
    text-align: center;
    font-family: "Cinzel", serif;
    font-weight: 500;
    font-size: 74px;
    line-height: 104px;
    background: linear-gradient(180deg, var(--gold-light), var(--gold) 45%, var(--gold-deep));
    -webkit-background-clip: text;
    background-clip: text;
    color: transparent;
  }
  .description {
    position: absolute;
    left: 48px;
    top: 650px;
    width: 380px;
    font-size: 19px;
    line-height: 26px;
    text-align: justify;
    text-align-last: center;
    color: var(--gold);
  }
  .call-out {
    position: absolute;
    left: 104px;
    top: 853px;
    width: 267px;
    height: 55px;
    border-radius: 28px;
    background: linear-gradient(180deg, var(--gold-light), var(--gold) 50%, var(--gold-deep));
    border: 2px solid var(--gold-deep);
    display: flex;
    align-items: center;
    justify-content: center;
    font-family: "Oswald", sans-serif;
    font-weight: 600;
    font-size: 36px;
    color: var(--ink-dark);
    letter-spacing: 0.5px;
  }
  .tagline {
    position: absolute;
    left: 0;
    top: 955px;
    width: 100%;
    text-align: center;
    font-size: 19px;
    line-height: 27px;
    color: var(--gold);
  }
  .volume-band {
    position: absolute;
    left: 0;
    bottom: 0;
    width: 100%;
    height: 52px;
    background: linear-gradient(180deg, var(--gold-light), var(--gold) 45%, var(--gold-deep));
    display: flex;
    align-items: center;
    justify-content: center;
    font-weight: 700;
    font-size: 25px;
    color: var(--ink-dark);
  }
</style>
</head>
<body>
  <main class="label">
    <svg class="brand-mark" viewBox="0 0 138 138" aria-hidden="true">
      <circle cx="69" cy="69" r="66" fill="none" stroke="#e2b624" stroke-width="4"/>
    </svg>
    <div class="brand-name">LUVRA</div>

    <h1 class="product-name">PRODUCT<br>NAME</h1>

    <p class="description">Lorem ipsum dolor sit amet, consectetur adipisicing elit, sed do eiusmod tempor incididunt ut labore et dolore magna aliqua. Ut enim ad minim veniam, quis nostrud exercitation.</p>

    <div class="call-out">TEXT HERE!</div>

    <p class="tagline">Lorem ipsum dolor sit amet,<br>consectetur adipisicing elit.</p>

    <div class="volume-band">150 ml | 8.4 oz</div>
  </main>
</body>
</html>
```